Velnor Group: Business Card for a high end technology company

We need a cool new design for our business cards using our cloud logo. We are a technology consulting business. We pride ourselves on be the best of the best. We mainly focus on cloud solutions and managed services. We need a business card that sets us apart from the other technology companies in the area and allows us to stand out.

Target Market(s)

Technology departments, CIO, CEOs, and Information Technology Staff.

Industry/Entity Type

Information Technology

Contact Information for Business Card

Must have the logo and our name.
Must have employee name, email address, office phone, cell phone and website.
Need to have all info on one side a cool design on backside.

Font styles to use
Serif
Sans Serif

Requirements
Must have
• Must have the logo and our name.
• Must have employee name, email address, office phone, cell phone and website.
• Need to have all info on one side a cool design on back side.
• Must be a crisp clean design, not too busy or confusing.

```html
<!DOCTYPE html>
<html lang="en">
<head>
<meta charset="utf-8">
<title>Velnor Group – Business Card</title>
<link rel="stylesheet" href="https://fonts.googleapis.com/css2?family=Open+Sans:wght@400;600&display=swap">
<style>
  :root {
    --backdrop: #e9e6e1;
    --card-white: #f7f7f7;
    --card-dark: #2a2a2b;
    --ink-dark: #3a3a3a;
    --ink-light: #e6e6e6;
    --ink-muted: #a9a9a9;
    --accent: #3ba3e6;
    --accent-deep: #1d6fc4;
    --accent-light: #63c3f0;
  }
  * { margin: 0; padding: 0; box-sizing: border-box; }
  html, body {
    width: 1200px; height: 1023px; overflow: hidden;
    background: var(--backdrop);
    font-family: "Open Sans", Arial, sans-serif;
  }
  .stage { position: relative; width: 1200px; height: 1023px; }
  .card {
    position: absolute; width: 520px; height: 298px;
    border-radius: 3px; overflow: hidden;
    box-shadow: 0 10px 28px rgba(0,0,0,0.22);
  }
  .card--front { left: 90px; top: 150px; background: var(--card-white); }
  .card--back { left: 590px; top: 575px; background: var(--card-dark); }
  .card__art { position: absolute; inset: 0; width: 100%; height: 100%; }

  .brand {
    position: absolute; display: flex; align-items: center; gap: 12px;
    font-weight: 400; letter-spacing: 0.5px;
  }
  .brand__dot { width: 18px; height: 18px; border-radius: 50%; background: var(--accent); }
  .card--front .brand { left: 38px; bottom: 46px; font-size: 34px; color: var(--ink-dark); }
  .card--back .brand { left: 50%; top: 100px; transform: translateX(-50%); font-size: 46px; color: #ffffff; white-space: nowrap; }

  .contact {
    position: absolute; right: 28px; top: 26px;
    text-align: right; color: var(--ink-light);
  }
  .contact__name { font-size: 22px; font-weight: 600; color: var(--accent); }
  .contact__role { font-size: 13px; color: var(--ink-muted); margin-bottom: 18px; }
  .contact__line { font-size: 14px; line-height: 24px; display: flex; justify-content: flex-end; align-items: center; gap: 8px; }
  .contact__icon { width: 11px; height: 11px; border-radius: 2px; background: var(--accent); }
  .contact__gap { height: 14px; }

  .website {
    position: absolute; left: 132px; top: 180px;
    font-size: 14px; letter-spacing: 1.5px; color: var(--ink-muted);
  }
</style>
</head>
<body>
<main class="stage">
  <section class="card card--front" aria-label="Business card front">
    <svg class="card__art" viewBox="0 0 520 298" preserveAspectRatio="none" aria-hidden="true">
      <defs>
        <linearGradient id="ribbon" x1="0" y1="0" x2="1" y2="1">
          <stop offset="0" stop-color="#1d6fc4"/>
          <stop offset="0.5" stop-color="#63c3f0"/>
          <stop offset="1" stop-color="#3ba3e6"/>
        </linearGradient>
      </defs>
      <path d="M150,0 C230,10 250,80 290,150 C330,220 360,290 440,298 L520,298 L520,0 Z" fill="#2a2a2b"/>
      <path d="M150,0 C230,10 250,80 290,150 C330,220 360,290 440,298 L410,298 C340,285 305,225 270,160 C235,95 215,25 130,0 Z" fill="url(#ribbon)"/>
    </svg>
    <div class="brand"><span class="brand__dot"></span>Velnor Group</div>
    <div class="contact">
      <p class="contact__name">Adrian Kessler</p>
      <p class="contact__role">Director</p>
      <p class="contact__line">(702)-555-0148 <span class="contact__icon"></span></p>
      <p class="contact__line">470.555.0192 <span class="contact__icon"></span></p>
      <p class="contact__line">info@velnorgroup.com <span class="contact__icon"></span></p>
      <div class="contact__gap"></div>
      <p class="contact__line">2400 Harlow Ave Suite 310</p>
      <p class="contact__line">Brenton, GA 30412</p>
    </div>
  </section>

  <section class="card card--back" aria-label="Business card back">
    <div class="brand"><span class="brand__dot"></span>Velnor Group</div>
    <p class="website">www.velnorgroup.com</p>
  </section>
</main>
</body>
</html>
```